Liquor Label / Aguardiente

Label design for liquor bottle. Designers may submit multiple submissions.

Product Description:
Name: Viento de Plata™
Alcohol Category: Aguardiente (which in Spanish most closely translates to “burning water”) – aguardiente is derived from
cane sugar and is a general term for a type of alcoholic spirit in many Central and South America countries.
Taste: A smooth liquor with a comfortable yet spicy finish
Smell: Subtle aroma of spicy jalapeños
Liquid Color: Clear
Bottle Color: Clear
See link for reference - http://www.kelvostamp.com/sites/default/files/styles/uc_product_full/public/Pemrow_0.jpg?itok=9QmT2xLp
Closure: Bar top / cork
Bottle Shape/Size: height = 8.67in; diameter of base = 3.70in; diameter of neck = 0.85in

Label may consist of two separate parts (i.e. front and back, front and vertical side), or one continuous label.

Designer has complete freedom with color, font etc. unless otherwise stated below. The label MUST
contain (but is not limited only to) the following text exactly as written in quotes below:
- “Viento de Plata”
- “Aguardiente”
- “Cane Neutral Spirit with Natural Flavors”
- “35% Alc./Vol.”
- “750 ml”
- “Bottled by WP Spirits, LLC” and “Nashville, TN” - “Government Warning: (1) According to the Surgeon General, women should not drink alcoholic beverages during
pregnancy because of the risk of birth defects. (2) Consumption of alcoholic beverages impairs your ability to
drive a car or operate machinery, and may cause health problems.” (text in previous quotes must be in all
capitalized letters, text must be 2 MM in height and quote must be separated 2MM by all other text)
- Must be dedicated empty space for bar code (approximately 0.75in. height x 1.25in. length)

Target Market(s)

Label should have mass market appeal.
Age: 21 – 28 years old (primary target market is 21+ year old college students and recent graduates)
Target Market Gender: Both male and female, with emphasis on male
Consumption Focus: Spirit will be consumed typically as a shot, primarily at bars and secondarily off premise (label design will be critical for making our product highly visible behind a bar)
Marketing Theme: South American elements. The official Viento de Plata mascot is a llama and the incorporation and use of a llama somewhere (however large or small) on the bottle is encourage but by no means required.

Industry/Entity Type

Health

Requirements
Should not have
• Elements that may lead a potential consumer to believe the beverage is a craft liquor or an artisan brand. Please do not include images of peppers.

```html
<!DOCTYPE html>
<html lang="en">
<head>
<meta charset="utf-8">
<title>Viento de Plata – Aguardiente Label</title>
<link rel="stylesheet" href="https://fonts.googleapis.com/css2?family=Josefin+Sans:wght@400;600;700&family=Montserrat:wght@400;600&family=Kaushan+Script&display=swap">
<style>
  :root {
    --stage: #e6e6e6;
    --label-black: #0d0606;
    --label-deep: #2a0a08;
    --drop-outer: #6e0d0b;
    --drop-inner: #a8140f;
    --drop-glow: #d8431c;
    --cream: #fbe6bd;
    --gold: #d9a441;
    --rule: #c9362a;
    --paper-text: #ece4d8;
    --mascot: #f4f1ec;
  }
  html, body {
    margin: 0;
    width: 1200px;
    height: 1200px;
    overflow: hidden;
    background: var(--stage);
  }
  .label {
    position: absolute;
    left: 237px;
    top: 51px;
    width: 726px;
    height: 1098px;
    display: block;
    box-shadow: 0 6px 24px rgba(0,0,0,.25);
  }
  .brand-name {
    font-family: "Josefin Sans", sans-serif;
    font-weight: 700;
    fill: var(--cream);
    text-anchor: middle;
  }
  .arc-small {
    font-family: "Josefin Sans", sans-serif;
    font-weight: 600;
    font-size: 15px;
    letter-spacing: 2px;
    fill: var(--gold);
  }
  .arc-category {
    font-family: "Josefin Sans", sans-serif;
    font-weight: 600;
    font-size: 28px;
    letter-spacing: 4px;
    fill: var(--gold);
  }
  .volume {
    font-family: "Kaushan Script", cursive;
    font-size: 19px;
    fill: var(--paper-text);
    text-anchor: middle;
  }
  .facts {
    font-family: "Montserrat", sans-serif;
    font-size: 13.5px;
    fill: var(--paper-text);
    text-anchor: middle;
    letter-spacing: .5px;
  }
  .facts-strong { font-weight: 600; }
  .warning {
    font-family: "Montserrat", sans-serif;
    font-size: 8px;
    fill: var(--gold);
    letter-spacing: .2px;
  }
</style>
</head>
<body>
<svg class="label" viewBox="0 0 660 998" xmlns="http://www.w3.org/2000/svg">
  <defs>
    <radialGradient id="label-bg" cx="50%" cy="45%" r="65%">
      <stop offset="0" stop-color="var(--label-deep)"/>
      <stop offset="1" stop-color="var(--label-black)"/>
    </radialGradient>
    <radialGradient id="drop-fill" cx="50%" cy="72%" r="60%">
      <stop offset="0" stop-color="var(--drop-glow)"/>
      <stop offset=".55" stop-color="var(--drop-inner)"/>
      <stop offset="1" stop-color="var(--drop-outer)"/>
    </radialGradient>
    <path id="arc-left" d="M52,560 Q105,705 262,738"/>
    <path id="arc-left-2" d="M38,580 Q92,745 260,772"/>
    <path id="arc-right" d="M372,760 Q545,725 622,545"/>
  </defs>

  <rect class="label-ground" width="660" height="998" fill="url(#label-bg)"/>

  <path class="flame-drop" d="M331,43 C300,140 62,330 62,485 C62,615 180,705 331,705 C482,705 600,615 600,485 C600,330 362,140 331,43Z" fill="var(--drop-outer)" opacity=".75"/>
  <path class="flame-drop-core" d="M331,105 C305,195 105,355 105,500 C105,610 205,685 331,685 C457,685 557,610 557,500 C557,355 357,195 331,105Z" fill="url(#drop-fill)"/>

  <g class="brand-mark">
    <text class="brand-name" x="331" y="400" font-size="80">Viento</text>
    <text class="brand-name" x="331" y="478" font-size="80">de</text>
    <text class="brand-name" x="331" y="572" font-size="80">Plata</text>
  </g>

  <text class="arc-small"><textPath href="#arc-left">CANE NEUTRAL SPIRIT</textPath></text>
  <text class="arc-small"><textPath href="#arc-left-2">WITH NATURAL FLAVORS</textPath></text>
  <text class="arc-category"><textPath href="#arc-right">AGUARDIENTE</textPath></text>

  <path class="ground-line" d="M0,832 C120,815 200,842 330,830 C460,818 560,840 660,824" fill="none" stroke="var(--rule)" stroke-width="1.6"/>

  <rect class="mascot-llama" role="img" aria-label="White silhouette of a standing llama, the brand mascot" x="270" y="735" width="96" height="110" rx="10" fill="var(--mascot)"/>

  <g class="product-facts">
    <text class="volume" x="555" y="766">750 ml</text>
    <line x1="490" y1="780" x2="620" y2="780" stroke="var(--paper-text)" stroke-width=".8"/>
    <text class="facts" x="555" y="806">35% Alc./Vol.</text>
    <line x1="490" y1="838" x2="620" y2="838" stroke="var(--paper-text)" stroke-width=".8"/>
    <text class="facts" x="555" y="866">BOTTLED BY</text>
    <line x1="490" y1="880" x2="620" y2="880" stroke="var(--paper-text)" stroke-width=".8"/>
    <text class="facts facts-strong" x="555" y="902">WP SPIRITS, LLC</text>
    <text class="facts" x="555" y="920">NASHVILLE, TN</text>
  </g>

  <g class="government-warning">
    <text class="warning" x="40" y="866">GOVERNMENT WARNING:</text>
    <text class="warning" x="40" y="884">(1)</text>
    <text class="warning" x="62" y="884">ACCORDING TO THE SURGEON GENERAL, WOMEN SHOULD NOT DRINK ALCOHOLIC</text>
    <text class="warning" x="62" y="894">BEVERAGES DURING PREGNANCY BECAUSE OF THE RISK OF BIRTH DEFECTS.</text>
    <text class="warning" x="40" y="911">(2)</text>
    <text class="warning" x="62" y="911">CONSUMPTION OF ALCOHOLIC BEVERAGES IMPAIRS YOUR ABILITY TO DRIVE A CAR</text>
    <text class="warning" x="62" y="921">OR OPERATE MACHINERY, AND MAY CAUSE HEALTH PROBLEMS.</text>
  </g>
</svg>
</body>
</html>
```